Maple Sprout Menu (Vegetarian Restaurant Concept)

Maple Sprout is a new concept fast casual restaurant
renders are attached so you can see the style of restaurant
Maple Sprowt is a vibrant and modern Vegetarian fast casual restaurant concept that mixes fresh food, energy, great décor, and a comfortable, welcoming atmosphere to provide a memorable and all Vegetarian dining experience.
Our Mission is to be top of mind when consumers think Vegetarian food!
Target Market(s)
the menu is vegetarian and appeals to a broad demographic in USA
Colors
Designer to choose colors to be used in the design.
Requirements
Must have
- well colored and well laid out menu - should not be cartoonish
Nice to have
- For Phots please use the shots in this file:
- https://www.filecrate-example.net/sh/kq7trm2wzl4pnad/BBBxT_qPwLdRNVoE_KMS_Tb?dl=0
- note these are untouched and you are free to change as needed
Should not have
- Should not be cartoonish - nor kives, forks etc in the design

```html
<!DOCTYPE html>
<html lang="en">
<head>
<meta charset="utf-8">
<title>Maple Sprowt — Menu</title>
<link href="https://fonts.googleapis.com/css2?family=Quicksand:wght@600;700&family=Montserrat:wght@500;800&display=swap" rel="stylesheet">
<style>
  :root {
    --leaf: #5b8a1f;
    --ink: #1d1d1d;
    --rule: #b9c38c;
    --paper: #ffffff;
  }
  * { margin: 0; padding: 0; box-sizing: border-box; }
  html, body { width: 1200px; height: 927px; overflow: hidden; background: var(--paper); }
  .menu-cover { position: relative; width: 1200px; height: 927px; font-family: "Quicksand", sans-serif; }

  .values-box {
    position: absolute; left: 23px; top: 331px; width: 345px; height: 273px;
    border: 1px dashed var(--rule);
  }
  .value {
    position: absolute; left: 0; width: 100%; text-align: center;
    color: var(--leaf); font-weight: 700; font-size: 14px; letter-spacing: 2.6px;
    transform: translateY(-50%);
  }
  .value-rule { position: absolute; left: 22px; right: 21px; border-top: 1px dashed var(--rule); }

  .website {
    position: absolute; top: 886px; left: 22px; width: 345px;
    display: flex; align-items: center; justify-content: space-between;
    transform: translateY(-50%);
  }
  .website span { color: var(--leaf); font-weight: 700; font-size: 13.5px; letter-spacing: 2.2px; }
  .website i { display: block; width: 59px; border-top: 1px dashed var(--rule); }

  .address-box {
    position: absolute; left: 434px; top: 783px; width: 332px; height: 115px;
    border: 1px dashed var(--rule); text-align: center;
    font-family: "Montserrat", sans-serif; color: var(--ink);
  }
  .address-box h2 { margin-top: 27px; font-weight: 800; font-size: 14px; letter-spacing: 2.8px; }
  .address-box p { font-weight: 500; font-size: 11.5px; letter-spacing: 2px; line-height: 21px; margin-top: 3px; }
  .address-box p + p { margin-top: 0; }

  .cover-frame { position: absolute; top: 29px; height: 700px; border-left: 1px dashed var(--rule); }
  .cover-frame.left { left: 820px; }
  .cover-frame.right-top { left: 1172px; height: 335px; }
  .cover-frame.right-bottom { left: 1172px; top: 524px; height: 205px; }

  .menu-title {
    position: absolute; left: 1169px; top: 446px;
    transform: translate(-50%, -50%) rotate(90deg);
    color: var(--leaf); font-weight: 700; font-size: 28px; letter-spacing: 8px;
  }

  .dish { position: absolute; width: 105px; height: 107px; }
  .dish.l { left: 885px; border-top-left-radius: 100% 100%; }
  .dish.r { left: 1002px; border-top-right-radius: 100% 100%; }
  .dish-rule { position: absolute; left: 885px; width: 222px; border-top: 2.5px dotted var(--leaf); }

  .brand {
    position: absolute; left: 995px; top: 650px; transform: translateX(-50%);
    display: flex; flex-direction: column; align-items: center; gap: 10px;
  }
  .brand-dot { width: 34px; height: 34px; border-radius: 50%; background: var(--leaf); }
  .brand-name { font-weight: 700; font-size: 26px; color: var(--ink); white-space: nowrap; }

  .panel-rule { position: absolute; left: 819px; top: 769px; width: 354px; border-top: 1px dashed var(--rule); }
  .info-box {
    position: absolute; left: 864px; width: 264px; height: 44px;
    border: 1px dashed var(--rule);
    display: flex; align-items: center; justify-content: center;
    font-family: "Montserrat", sans-serif; font-weight: 800; font-size: 12px; letter-spacing: 2.2px; color: var(--ink);
  }
</style>
</head>
<body>
<main class="menu-cover">

  <section class="values-box">
    <div class="value" style="top:40px">100% VEGETARIAN</div>
    <div class="value-rule" style="top:62px"></div>
    <div class="value" style="top:86px">LOCALLY SOURCED</div>
    <div class="value-rule" style="top:111px"></div>
    <div class="value" style="top:135px">FRESH</div>
    <div class="value-rule" style="top:160px"></div>
    <div class="value" style="top:185px">ORGANIC</div>
    <div class="value-rule" style="top:209px"></div>
    <div class="value" style="top:232px">HIGH QUALITY INGREDIENTS</div>
  </section>

  <div class="website"><i></i><span>www.maplesprowt.com</span><i></i></div>

  <section class="address-box">
    <h2>THE COMMONS AT ALDER RIDGE</h2>
    <p>4120 ALDER RIDGE ROAD</p>
    <p>BROOKFIELD VILLAGE, CA 90000</p>
  </section>

  <div class="cover-frame left"></div>
  <div class="cover-frame right-top"></div>
  <div class="cover-frame right-bottom"></div>
  <div class="menu-title">MENU</div>

  <div class="dish l" style="top:80px;background:linear-gradient(135deg,#8fa33a,#c9c08a 55%,#4f6a22)" role="img" aria-label="Salad with corn, black beans and crumbled cheese"></div>
  <div class="dish r" style="top:80px;background:linear-gradient(135deg,#6b1a2a,#b0233f 55%,#4a6b2a)" role="img" aria-label="Diced beet salad with fresh herbs"></div>
  <div class="dish-rule" style="top:190px"></div>

  <div class="dish l" style="top:201px;background:linear-gradient(135deg,#6f8f2f,#a9b760 50%,#3d2a1e)" role="img" aria-label="Kale salad with croutons and dried cranberries"></div>
  <div class="dish r" style="top:201px;background:linear-gradient(135deg,#3f6a1f,#6e9a34 55%,#b2322a)" role="img" aria-label="Edamame and green bean salad with red pepper"></div>
  <div class="dish-rule" style="top:310px"></div>

  <div class="dish l" style="top:321px;background:linear-gradient(135deg,#d84a2c,#e8b43a 55%,#f1d878)" role="img" aria-label="Corn and tomato flatbread"></div>
  <div class="dish r" style="top:321px;background:linear-gradient(135deg,#e6dcc6,#6c8d3a 55%,#b04048)" role="img" aria-label="Stuffed pita with greens and vegetables"></div>
  <div class="dish-rule" style="top:430px"></div>

  <div class="dish l" style="top:441px;background:linear-gradient(135deg,#9b5e3c,#8fa83e 55%,#3a2a1e)" role="img" aria-label="Avocado salad with almonds and balsamic glaze"></div>
  <div class="dish r" style="top:441px;background:linear-gradient(135deg,#c79a6a,#6a3f28 55%,#b4b79a)" role="img" aria-label="Veggie burger with sauce and slaw"></div>
  <div class="dish-rule" style="top:550px"></div>

  <div class="brand">
    <span class="brand-dot"></span>
    <span class="brand-name">Maple Sprowt</span>
  </div>

  <div class="panel-rule"></div>
  <div class="info-box" style="top:797px">(555) 014-2290</div>
  <div class="info-box" style="top:849px">MON-SAT: 11AM - 9PM</div>

</main>
</body>
</html>
```